Business Card Design

I need a business card for my rental business. The business is named:
Hire a Vorlatrike Brenmoor
www.hireavorlatrikebrenmoor.example
(555) 014-2937
This will be a business card that I will leave at other businesses as advertisement so it needs to have the name, website, and phone number.
Please feel free to be creative. This is a new business so I have no designs.
Thank you very much for your time and I look forward to receiving your designs
Target Market(s)
Local rental customers
Industry/Entity Type
Business
Contact Information for Business Card
Please check out my website:
Other font styles liked:
- anything creative
Colors
Designer to choose colors to be used in the design.
Requirements
Must have
- Business name, phone, website. Rentals available hourly or daily. Book online

```html
<!DOCTYPE html>
<html lang="en">
<head>
<meta charset="utf-8">
<title>Hire a Vorlatrike Brenmoor – Business Card</title>
<link rel="stylesheet" href="https://fonts.googleapis.com/css2?family=Oswald:wght@500&family=Roboto:wght@400&family=Roboto+Condensed:wght@500&display=swap">
<style>
  :root {
    --page: #ffffff;
    --card-white: #ffffff;
    --slate: #6d6e71;
    --ink: #5f6063;
    --edge: #e2e2e2;
  }
  html, body {
    margin: 0;
    padding: 0;
    width: 1200px;
    height: 1200px;
    overflow: hidden;
    background: var(--page);
  }
  .canvas {
    position: relative;
    width: 1200px;
    height: 1200px;
  }
  .card {
    position: absolute;
    left: 304px;
    width: 636px;
    height: 362px;
    border-radius: 17px;
    overflow: hidden;
  }
  .card--front {
    top: 232px;
    background: var(--card-white);
    border: 1px solid var(--edge);
    box-sizing: border-box;
  }
  .card--back {
    top: 636px;
    background: var(--slate);
  }
  .brand-name {
    position: absolute;
    left: 0;
    right: 0;
    margin: 0;
    text-align: center;
    font-family: "Oswald", sans-serif;
    font-weight: 500;
    letter-spacing: 0.5px;
    white-space: nowrap;
  }
  .card--front .brand-name {
    top: 58px;
    font-size: 36px;
    color: var(--slate);
  }
  .card--back .brand-name {
    top: 150px;
    font-size: 42px;
    color: var(--card-white);
  }
  .contact {
    position: absolute;
    top: 168px;
    left: 0;
    right: 0;
    margin: 0;
    padding: 0;
    list-style: none;
    text-align: center;
    font-family: "Roboto", sans-serif;
    font-size: 20px;
    line-height: 33px;
    color: var(--ink);
  }
  .offer-band {
    position: absolute;
    left: 0;
    right: 0;
    bottom: 0;
    height: 85px;
    background: var(--slate);
    color: var(--card-white);
    font-family: "Roboto Condensed", sans-serif;
    font-weight: 500;
    font-size: 21px;
    line-height: 32px;
    text-align: center;
    padding-top: 10px;
    box-sizing: border-box;
  }
  .offer-band p { margin: 0; }
</style>
</head>
<body>
<main class="canvas">
  <section class="card card--front" aria-label="Business card front">
    <h1 class="brand-name">HIRE A VORLATRIKE BRENMOOR</h1>
    <ul class="contact">
      <li class="contact__phone">(555) 014-2937</li>
      <li class="contact__web">www.hireavorlatrikebrenmoor.example</li>
      <li class="contact__address">Route 418, Brenmoor, Calder 60412, United States</li>
    </ul>
    <div class="offer-band">
      <p>Rentals available hourly or daily</p>
      <p>Book Online</p>
    </div>
  </section>

  <section class="card card--back" aria-label="Business card back">
    <h2 class="brand-name">HIRE A VORLATRIKE BRENMOOR</h2>
  </section>
</main>
</body>
</html>
```